NOTE: I PROVIDED THE INCORRECT LOGO AND ONLY A HANDFUL OF PEOPLE NOTICED THAT IT WAS NOT THE ONE I DESCRIBED. THE LOGO I HAVE NOW ATTACHED MATCHES MY WEBSITE AND THE COLORS ON THE WEBSITE SHOULD BE USED FOR THE CARD.

PLEASE READ THE BUSINESS CARD DETAILS AND PROJECT MUST HAVES CAREFULLY.

I am looking for a business card that is powerful, a bit edgy, and although I work in the corporate world, not too formal. I would like to see designs that use the colors on my website www.brightlumo.com. I don't want the card to look washed out so please use shades of those colors that make them "pop". The "vibe" of the card needs to show substance and confidence while also reflecting that we're not your usual consultants.

The focus of my work is turning "people problems" into profits. Those problems could be poor service, an unstable workforce, untrained leaders, or managing change. We are an aggressive, results-focused team of performance improvement professionals who refuse to believe "things can't be done". For us, failure is not an option. Our logo reflects a target from the view of the site on a gun.

In addition to the contact information provided on the sample business card (do not include "turning people problems into profits"), I would like to include this statement (probably on the back):
I equip results-oriented business leaders to turn their people problems into profits in six months or less.

PLEASE NOTE THAT MY WEBSITE IS UNDER REVISION TO TONE DOWN THE MILITARY THEME, ALTHOUGH THE WARRIOR ENERGY AND FOCUS ON RESULTS REMAINS.

Target Market(s)

My clients are Mid and senior-level managers. I don't target any particular industry.

Industry/Entity Type

Consulting

Contact Information for Business Card

In addition to the contact information provided on the sample business card (DO NOT INCLUDE "turning people problems into profits"), I would like to include this statement (probably on the back):

I don't care whether the card is landscape or portrait view.

Font styles to use
Sans Serif

Requirements
Must have
• 1. be easy to read, no 6-8 point fonts!
• 2. a "vibe" that captures the eye without being too chaotic or busy
• 3. bold color, not washed out or boring - a good blend with the colors currently on my website (black, red, white, army green) but you don't need to use all of them.
• 4. all the contact information I have provided
• 5. a good blend with the colors currently on my website
• 6. Must have this quote on the back of the card: I equip results-oriented business leaders to turn their people problems into profits in six months or less.
Nice to have
• In looking at the sample images I provided for ideas, you can see that I like the way a card carries over from one side to the next.
• It would be great to find some aspect/quality/feature that I haven't seen before
Should not have
• 1. NO use of ALL CAPS
• 2. fonts that I would have to seek out and purchase (you should provide files for font if using something not standard)

```html
<!DOCTYPE html>
<html lang="en">
<head>
<meta charset="UTF-8">
<title>Brightlumo Partners – Business Card</title>
<link rel="stylesheet" href="https://fonts.googleapis.com/css2?family=Questrial&family=Open+Sans:wght@400;700&display=swap">
<style>
  :root {
    --backdrop: #3b4048;
    --card: #161616;
    --army: #8fa83a;
    --army-deep: #5f7a2a;
    --red: #e0262b;
    --white: #ffffff;
  }
  * { margin: 0; padding: 0; box-sizing: border-box; }
  html, body {
    width: 1200px; height: 900px; overflow: hidden;
    background: var(--backdrop);
    font-family: "Questrial", "Century Gothic", sans-serif;
  }
  .canvas { position: relative; width: 1200px; height: 900px; }
  .card {
    position: absolute; left: 290px;
    width: 620px; height: 354px;
    background: var(--card);
    border-radius: 4px;
    box-shadow: 0 10px 30px rgba(0,0,0,.45);
    overflow: hidden;
  }
  .card--front { top: 60px; }
  .card--back { top: 486px; }

  /* front */
  .brand {
    position: absolute; left: 150px; top: 48px;
    display: flex; align-items: center; gap: 14px;
  }
  .brand__name { font-size: 44px; color: var(--army); line-height: 1; }
  .brand__mark { width: 24px; height: 24px; background: var(--red); }
  .person { position: absolute; left: 150px; top: 122px; }
  .person__name {
    font-family: "Open Sans", sans-serif; font-weight: 700;
    font-size: 30px; color: var(--white);
  }
  .person__title { font-size: 20px; color: var(--army); margin-top: 2px; }
  .divider {
    position: absolute; left: 40px; right: 40px; top: 222px;
    height: 2px; background: var(--red);
  }
  .contact {
    position: absolute; top: 244px;
    font-family: "Open Sans", sans-serif; font-size: 18px;
    color: var(--white); line-height: 1.6;
  }
  .contact--phones { left: 40px; }
  .contact--web { right: 40px; }
  .contact__label { color: var(--army); }

  /* back */
  .statement {
    position: absolute; left: 40px; top: 96px; width: 400px;
    font-size: 24px; line-height: 1.4;
  }
  .statement__lead { color: var(--white); }
  .statement__mid { color: var(--army); }
  .statement__end { color: var(--red); }
  .back-brand {
    position: absolute; right: 40px; top: 158px;
    display: flex; align-items: center; gap: 10px;
  }
  .back-brand__name { font-size: 26px; color: var(--army); }
  .back-brand__mark { width: 20px; height: 20px; background: var(--red); }
  .accent { position: absolute; }
  .accent--top { right: 150px; top: 0; }
  .accent--bottom { left: 70px; bottom: 0; }
</style>
</head>
<body>
<div class="canvas">
  <section class="card card--front">
    <div class="brand">
      <span class="brand__name">Brightlumo Partners</span>
      <span class="brand__mark"></span>
    </div>
    <div class="person">
      <div class="person__name">Dana Whitfield</div>
      <div class="person__title">Chief Performance Strategist</div>
    </div>
    <div class="divider"></div>
    <div class="contact contact--phones">
      <div><span class="contact__label">Work:</span> 248-555-0142</div>
      <div><span class="contact__label">Cell:</span> 248-555-0187</div>
    </div>
    <div class="contact contact--web">
      <div>danaw@brightlumo.com</div>
      <div>www.brightlumo.com</div>
    </div>
  </section>

  <section class="card card--back">
    <svg class="accent accent--top" width="30" height="18" viewBox="0 0 30 18"><polygon points="0,0 30,0 15,18" fill="var(--army)"/></svg>
    <p class="statement">
      <span class="statement__lead">I equip results-oriented business leaders</span>
      <span class="statement__mid">to turn their people problems into</span>
      <span class="statement__end">profits in six months or less.</span>
    </p>
    <div class="back-brand">
      <span class="back-brand__mark"></span>
      <span class="back-brand__name">Brightlumo</span>
    </div>
    <svg class="accent accent--bottom" width="30" height="20" viewBox="0 0 30 20"><polygon points="15,0 30,20 0,20" fill="var(--red)"/></svg>
  </section>
</div>
</body>
</html>
```